Velmoran Tabletop Deck Company (southern african focus for now) needs a e-commerce website

We need a website design for a playing card company based in Southern Africa/United States. We make locally-sourced playing cards (standard 52 card deck, with customized fronts and backs) for everyone and collaborate with local artists to uplift their talents, while celebrating their nation's culture, heritage, beauty and identity. We would like to see designs that use the colours blue (see flag of Eswatini as starting product), white and some red accents (or your recommendation). The final design should communicate elegance, fun and sustainable prosperity.

Target Market(s)

Everyone loves playing cards. From the solo adventurer to the party host, first time learner or expert, young, middle and old, we need to attract a broad audience that appreciates the finer things and supports sustainable, environmentally contentiousness causes that support the local economy and uplift local talent - thing global, act local.

Number of Pages Required

4 page

Font styles to use
Serif
Sans Serif

Requirements
Must have
• Pages to include Home (Main), About (Our Story), Shop and Contact
Nice to have
• While designs may be static, elements of graceful movement would be desirable. Perhaps functionality of scrolling down on homepage showing playing cards in use, front and back. Quindle and Zorbix store's capture that elegant yet rich look.
Should not have
• Too many products. We focus on 1-2.

```html
<!DOCTYPE html>
<html lang="en">
<head>
<meta charset="utf-8">
<title>Velmoran — Collections</title>
<link href="https://fonts.googleapis.com/css2?family=Poppins:wght@400;500&family=Prata&display=swap" rel="stylesheet">
<style>
:root{
  --ink:#1f1f1f;
  --muted:#555;
  --page:#f4f4f4;
  --card:#e9e9e9;
  --dark:#333333;
  --white:#ffffff;
  --flag-blue:#4a6fd1;
  --flag-red:#c9302c;
  --flag-gold:#f2c94c;
  --line:#bdbdbd;
}
*{box-sizing:border-box;margin:0;padding:0}
html,body{width:875px;height:1200px;overflow:hidden}
body{background:var(--page);font-family:"Poppins",sans-serif;color:var(--ink);position:relative}

.site-header{position:absolute;top:0;left:0;width:875px;height:76px;background:var(--dark);color:var(--white)}
.brand{position:absolute;left:64px;top:26px;font-family:"Prata",serif;font-size:18px;letter-spacing:.2px;display:flex;align-items:center;gap:7px}
.brand-dot{width:12px;height:12px;border-radius:50%;background:var(--white)}
.main-nav{position:absolute;top:32px;left:0}
.main-nav a{position:absolute;white-space:nowrap;color:var(--white);text-decoration:none;font-size:11.5px;font-weight:500}
.main-nav .is-active{border-bottom:1px solid var(--white);padding:0 3px 1px}
.region-select{position:absolute;left:704px;top:28px;width:107px;height:30px;border:1.5px solid var(--white);display:flex;align-items:center;padding-left:10px;gap:7px;font-size:11.5px}
.region-flag{width:15px;height:15px;border-radius:50%;overflow:hidden;border:1px solid var(--white)}
.caret{width:0;height:0;border-left:4.5px solid transparent;border-right:4.5px solid transparent;border-top:5px solid var(--white);margin-left:6px}

.filters{position:absolute;top:99px;left:0;width:875px;height:22px;font-size:11.5px;font-weight:500}
.filter-label{position:absolute;top:3px}
.filter-select{position:absolute;top:0;height:22px;border:1.3px solid var(--line);border-radius:12px;padding-left:11px;line-height:20px;font-weight:400;background:var(--white)}
.filter-select::after{content:"";position:absolute;right:9px;top:8px;border-left:4px solid transparent;border-right:4px solid transparent;border-top:5px solid #9a9a9a}

.product-grid{position:absolute;left:65px;top:163px;display:grid;grid-template-columns:repeat(3,224px);column-gap:37px;row-gap:60px}
.product-card{height:237px;background:var(--card);border-radius:19px;box-shadow:2px 4px 6px rgba(0,0,0,.14);text-align:center;position:relative}
.product-image{position:absolute;left:18px;top:22px;width:188px;height:120px;border-radius:8px;background:linear-gradient(90deg,#f4f4f4 0 30%,#5b7fd6 30% 42%,#c9302c 42% 82%,#5b7fd6 82% 100%)}
.product-name{position:absolute;top:181px;left:0;right:0;font-size:16.5px;font-weight:500}
.product-price{position:absolute;top:205px;left:0;right:0;font-size:15px;color:var(--muted)}

.pagination{position:absolute;top:1034px;left:0;width:875px;height:30px;font-size:11.5px;color:#333}
.pagination span{position:absolute;top:7px;transform:translateX(-50%)}
.pagination .is-current{top:0;width:30px;height:30px;border-radius:50%;background:#e3e3e3;text-align:center;line-height:30px}
.pagination .arrow{color:#999;font-size:14px;top:5px}
.pagination .arrow.next{color:#333}

.site-footer{position:absolute;top:1086px;left:0;width:875px;height:114px;background:var(--dark);color:var(--white)}
.footer-brand{position:absolute;left:49px;top:22px;font-family:"Prata",serif;font-size:33px;display:flex;align-items:center;gap:12px}
.footer-brand .brand-dot{width:30px;height:30px}
.footer-links{position:absolute;left:332px;top:26px;font-size:9px;line-height:21.5px}
.footer-contacts{position:absolute;left:439px;top:26px;font-size:9px;line-height:21.5px}
.footer-contacts li,.footer-links li{list-style:none;display:flex;align-items:center;gap:6px;height:21.5px}
.footer-contacts svg{width:10px;height:10px}
.social-list{position:absolute;left:606px;top:26px;display:flex;gap:23px}
.social-list li{list-style:none;width:35px;height:35px;border:2px solid var(--white);border-radius:50%}
.copyright{position:absolute;left:605px;top:1156px;font-size:7.5px;color:var(--white)}
</style>
</head>
<body>
<header class="site-header">
  <div class="brand"><span class="brand-dot"></span>Velmoran</div>
  <nav class="main-nav">
    <a style="left:254px" href="#">Home</a>
    <a style="left:329px" href="#">About</a>
    <a style="left:402px" class="is-active" href="#">Collections</a>
    <a style="left:511px" href="#">Contact</a>
  </nav>
  <div class="region-select">
    <svg class="region-flag" viewBox="0 0 16 16" aria-hidden="true">
      <rect width="16" height="16" fill="#4a6fd1"/><rect y="4" width="16" height="8" fill="#f2c94c"/><rect y="5" width="16" height="6" fill="#c9302c"/><ellipse cx="8" cy="8" rx="3" ry="2" fill="#fff"/>
    </svg>
    <span>Eswatini</span><span class="caret"></span>
  </div>
</header>

<section class="filters">
  <span class="filter-label" style="left:64px">Categories:</span>
  <div class="filter-select" style="left:138px;width:120px">All</div>
  <span class="filter-label" style="left:627px">Sort by:</span>
  <div class="filter-select" style="left:676px;width:134px">Popular</div>
</section>

<main class="product-grid">
  <article class="product-card"><div class="product-image" role="img" aria-label="Eswatini playing card deck box with ace of hearts"></div><h2 class="product-name">Eswatini Playing Cards</h2><p class="product-price">$ 10.00</p></article>
  <article class="product-card"><div class="product-image" role="img" aria-label="Eswatini playing card deck box with ace of hearts"></div><h2 class="product-name">Eswatini Playing Cards</h2><p class="product-price">$ 10.00</p></article>
  <article class="product-card"><div class="product-image" role="img" aria-label="Eswatini playing card deck box with ace of hearts"></div><h2 class="product-name">Eswatini Playing Cards</h2><p class="product-price">$ 10.00</p></article>
  <article class="product-card"><div class="product-image" role="img" aria-label="Eswatini playing card deck box with ace of hearts"></div><h2 class="product-name">Eswatini Playing Cards</h2><p class="product-price">$ 10.00</p></article>
  <article class="product-card"><div class="product-image" role="img" aria-label="Eswatini playing card deck box with ace of hearts"></div><h2 class="product-name">Eswatini Playing Cards</h2><p class="product-price">$ 10.00</p></article>
  <article class="product-card"><div class="product-image" role="img" aria-label="Eswatini playing card deck box with ace of hearts"></div><h2 class="product-name">Eswatini Playing Cards</h2><p class="product-price">$ 10.00</p></article>
  <article class="product-card"><div class="product-image" role="img" aria-label="Eswatini playing card deck box with ace of hearts"></div><h2 class="product-name">Eswatini Playing Cards</h2><p class="product-price">$ 10.00</p></article>
  <article class="product-card"><div class="product-image" role="img" aria-label="Eswatini playing card deck box with ace of hearts"></div><h2 class="product-name">Eswatini Playing Cards</h2><p class="product-price">$ 10.00</p></article>
  <article class="product-card"><div class="product-image" role="img" aria-label="Eswatini playing card deck box with ace of hearts"></div><h2 class="product-name">Eswatini Playing Cards</h2><p class="product-price">$ 10.00</p></article>
</main>

<nav class="pagination" aria-label="Pages">
  <span class="arrow" style="left:347px">&#8249;</span>
  <span class="is-current" style="left:375px">1</span>
  <span style="left:404px">2</span>
  <span style="left:435px">3</span>
  <span style="left:466px">4</span>
  <span style="left:498px">...</span>
  <span class="arrow next" style="left:528px">&#8250;</span>
</nav>

<footer class="site-footer">
  <div class="footer-brand"><span class="brand-dot"></span>Velmoran</div>
  <ul class="footer-links">
    <li>Corporate office</li><li>International Branch</li><li>Contact Us</li>
  </ul>
  <ul class="footer-contacts">
    <li><svg viewBox="0 0 10 10" aria-hidden="true"><circle cx="5" cy="5" r="4.2" fill="none" stroke="#fff" stroke-width="1"/><path d="M3.5 3.3 L4.2 3 L4.7 4 L4.3 4.5 Q5 5.8 5.8 6 L6.3 5.6 L7 6.2 L6.6 6.9 Q4 6.8 3.5 3.3Z" fill="#fff"/></svg>+268 7000 4815</li>
    <li><svg viewBox="0 0 10 10" aria-hidden="true"><circle cx="5" cy="5" r="4.2" fill="none" stroke="#fff" stroke-width="1"/><path d="M3.5 3.3 L4.2 3 L4.7 4 L4.3 4.5 Q5 5.8 5.8 6 L6.3 5.6 L7 6.2 L6.6 6.9 Q4 6.8 3.5 3.3Z" fill="#fff"/></svg>+268 7000 4815</li>
    <li><svg viewBox="0 0 10 10" aria-hidden="true"><rect x="0.8" y="2" width="8.4" height="6" fill="none" stroke="#fff" stroke-width="1"/><path d="M1 2.3 L5 5.3 L9 2.3" fill="none" stroke="#fff" stroke-width="1"/></svg>hello@velmoran.com</li>
  </ul>
  <ul class="social-list" aria-label="Social channels">
    <li></li><li></li><li></li><li></li>
  </ul>
</footer>
<p class="copyright">© All Rights Reserved. Velmoran. 2020</p>
</body>
</html>
```